Vexo App

We want to have a web banner (4-5 slides) flash or whatever.
We are innovative next generation messenger with a good design, themes, snap mode, pinging and other features.
Inspired by night, by techno music, by energy, by innovations and next generation.
High tech.

The name of the app : Vexo
vexoapp.example

The banner will be used for nightlisting.example

We want the banner to be creative, and deliver the inspiration of the app.

All the assets, logos and so on can me delivered to you via email by request.

```html
<!DOCTYPE html>
<html lang="en">
<head>
<meta charset="utf-8">
<title>Vexo App – Web Banner</title>
<link rel="stylesheet" href="https://fonts.googleapis.com/css2?family=Montserrat:wght@500;600;700&display=swap">
<style>
  :root {
    --stage-bg: #535c64;
    --frame: #ffffff;
    --night-deep: #0a1440;
    --night-blue: #1a3a8a;
    --neon-teal: #1f7a6a;
    --neon-green: #3f9a10;
    --neon-lime: #8fbf10;
    --neon-yellow: #b8c81a;
    --text-light: #ffffff;
    --brand-square: #4cc4f4;
    --cta-top: #b6ecfc;
    --cta-bottom: #37b1ea;
    --cta-edge: #e8f8ff;
    --cta-text: #0d2533;
  }
  * { margin: 0; padding: 0; box-sizing: border-box; }
  html, body {
    width: 1200px;
    height: 900px;
    overflow: hidden;
    background: var(--stage-bg);
    font-family: "Montserrat", Arial, sans-serif;
  }
  .stage {
    position: relative;
    width: 1200px;
    height: 900px;
  }
  .banner {
    position: absolute;
    left: 52px;
    top: 381px;
    width: 1096px;
    height: 138px;
    border: 1.5px solid var(--frame);
    overflow: hidden;
  }
  .banner__backdrop {
    position: absolute;
    inset: 0;
    background:
      radial-gradient(ellipse at 25% 60%, rgba(40,140,200,0.45), transparent 55%),
      radial-gradient(ellipse at 85% 40%, rgba(210,220,40,0.45), transparent 60%),
      linear-gradient(90deg,
        var(--night-deep) 0%,
        var(--night-blue) 14%,
        var(--neon-teal) 26%,
        var(--neon-green) 44%,
        var(--neon-lime) 70%,
        var(--neon-yellow) 86%,
        var(--neon-lime) 100%);
  }
  .brand {
    position: absolute;
    left: 20px;
    top: 22px;
    display: flex;
    align-items: center;
    gap: 20px;
  }
  .brand__square {
    width: 92px;
    height: 92px;
    background: var(--brand-square);
    border-radius: 10px;
  }
  .brand__name {
    color: var(--text-light);
    font-weight: 700;
    font-size: 52px;
    letter-spacing: -1px;
  }
  .message {
    position: absolute;
    left: 348px;
    top: 10px;
    color: var(--text-light);
  }
  .message__headline {
    font-weight: 700;
    font-size: 51px;
    line-height: 1.1;
    letter-spacing: -0.5px;
  }
  .message__body {
    margin-top: 6px;
    font-weight: 600;
    font-size: 21px;
    line-height: 1.5;
  }
  .cta {
    position: absolute;
    left: 864px;
    top: 35px;
    width: 206px;
    height: 70px;
    border-radius: 10px;
    border: 2px solid var(--cta-edge);
    background: linear-gradient(180deg, var(--cta-top), var(--cta-bottom));
    display: flex;
    align-items: center;
    justify-content: center;
    color: var(--cta-text);
    font-weight: 500;
    font-size: 27px;
    box-shadow: 0 2px 6px rgba(0,0,0,0.3);
  }
</style>
</head>
<body>
  <main class="stage">
    <section class="banner">
      <div class="banner__backdrop" role="img" aria-label="Night-time neon light streaks shifting from deep blue to green and yellow"></div>
      <div class="brand">
        <span class="brand__square"></span>
        <span class="brand__name">Vexo</span>
      </div>
      <div class="message">
        <h1 class="message__headline">Inspired by night!</h1>
        <p class="message__body">New groundbreaking messenger<br>for your mobile now available!</p>
      </div>
      <a class="cta">Try it now!</a>
    </section>
  </main>
</body>
</html>
```